Lift Her Summit - Marketing Graphic Needed

Non-profit needs a full page and header size graphic for our 2023 Lift Her Summit.

The theme this year is: Unrestrained
Date: January 27, 2023
Location: Harborlight Stays Meeting Hall | San Marcos, TX
Focus (not to be included on flyer): identifying what's holding us back; moving forward; practice makes progress; creating new paradigms; dispelling self-sabotage; clarifying goals; how to kick butt and play to win; being true to your self; building self-confidence; working less to get more.

Target Market(s)

Women in the design and construction industry (architects, engineers, project managers, project Owners, attorneys)

Industry/Entity Type

Design and Construction

Requirements
Must have
• Title of Forum, Theme, date, location, Q-BraTM logo and Lift Her logo
Nice to have
• a graphic that exemplifies the theme: "Unrestrained"

```html
<!DOCTYPE html>
<html lang="en">
<head>
<meta charset="utf-8">
<title>Lift Her Summit 2023 – Unrestrained</title>
<link href="https://fonts.googleapis.com/css2?family=Kaushan+Script&family=Montserrat:ital,wght@0,300;0,400;0,500;0,600;0,700;1,600&display=swap" rel="stylesheet">
<style>
  :root{
    --stage:#6b6b6b;
    --navy:#1b2a78;
    --royal:#2c45a8;
    --deep:#12195a;
    --lime:#c9dc1f;
    --white:#ffffff;
    --ink:#2d2d2d;
    --site-blue:#2c4fa0;
    --site-green:#7fb23a;
    --orange:#f0a21a;
    --footer:#16306b;
    --sky-light:#8fa9e6;
    --sky-mid:#4c66c2;
    --steel:#b8c2d6;
    --deck:#1a1f3d;
  }
  *{margin:0;padding:0;box-sizing:border-box}
  html,body{width:1200px;height:2176px;overflow:hidden}
  body{background:var(--white);font-family:"Montserrat",Arial,sans-serif;position:relative}

  .stage{position:absolute;left:0;top:0;width:1200px;height:760px;background:var(--stage)}

  .banner{position:absolute;overflow:hidden;
    background:linear-gradient(120deg,var(--royal) 0%,var(--navy) 55%,var(--deep) 100%)}
  .banner--header{left:68px;top:32px;width:1052px;height:656px;font-size:16px}
  .banner--page{left:32px;top:1400px;width:1136px;height:652px;font-size:16.5px}

  .banner__visual{position:absolute;left:36%;top:0;width:64%;height:100%;
    background:
      radial-gradient(ellipse 38% 30% at 78% 22%,rgba(200,214,245,.85) 0%,rgba(200,214,245,0) 100%),
      linear-gradient(135deg,rgba(184,194,214,0) 30%,rgba(184,194,214,.35) 42%,rgba(184,194,214,0) 54%),
      linear-gradient(180deg,var(--sky-light) 0%,var(--sky-mid) 40%,var(--navy) 66%,var(--deck) 78%,#2b3566 100%);
    -webkit-mask-image:linear-gradient(90deg,transparent 0%,#000 30%);
    mask-image:linear-gradient(90deg,transparent 0%,#000 30%)}

  .banner__copy{position:absolute;left:4.5%;top:6%;width:44%;z-index:2}
  .banner__theme{font-family:"Kaushan Script",cursive;color:var(--lime);font-size:4.9em;line-height:1}
  .banner__year{font-family:"Montserrat",sans-serif;font-weight:400;color:var(--lime);font-size:10em;line-height:1;letter-spacing:.01em}
  .banner__rule{height:3px;background:var(--white);width:90%;margin:.5em 0 .8em}
  .banner__title{color:var(--white);font-weight:700;font-size:1.85em;line-height:1.2}
  .banner__date{color:var(--white);font-weight:400;font-size:2.4em;line-height:1.3}
  .banner__venue{color:var(--white);font-weight:600;font-size:.9em;margin-top:.5em;display:flex;align-items:center;gap:.4em;white-space:nowrap}
  .banner__venue svg{width:1em;height:1.2em;flex:none}

  .banner__logo{position:absolute;left:2.5%;bottom:4%;width:25%;height:13%;background:var(--white);
    display:flex;align-items:center;gap:.6em;padding:0 1em;z-index:2}
  .banner__logo-dot{width:2.4em;height:2.4em;border-radius:50%;background:var(--site-blue);flex:none}
  .banner__logo-name{font-weight:700;color:var(--site-blue);font-size:2.2em}

  .site-head{position:absolute;left:0;top:760px;width:1200px;height:208px;background:var(--white)}
  .site-logo{position:absolute;left:28px;top:44px;display:flex;align-items:center;gap:18px}
  .site-logo__dot{width:110px;height:110px;border-radius:50%;background:var(--site-green)}
  .site-logo__name{font-weight:700;color:var(--site-blue);font-size:72px}
  .site-login{position:absolute;right:22px;top:46px;font-size:18px;color:var(--ink)}
  .site-search{position:absolute;right:22px;top:106px;width:240px;height:36px;border:1px solid #bbb;border-radius:4px;
    font-size:16px;color:#888;display:flex;align-items:center;gap:8px;padding-left:10px}

  .site-nav{position:absolute;left:0;top:968px;width:1200px;height:64px;border-top:1px solid #ddd;
    display:flex;align-items:center;gap:30px;padding:0 14px;font-size:17px;font-weight:600;color:var(--ink);white-space:nowrap}
  .site-nav__home{color:var(--site-blue);border-bottom:3px solid var(--site-blue);padding-bottom:6px}
  .site-nav__caret{font-size:.7em;color:var(--site-blue);margin-left:4px}
  .site-nav__menu{margin-left:auto;display:flex;flex-direction:column;gap:5px}
  .site-nav__menu span{display:block;width:26px;height:4px;background:var(--ink)}

  .mission{position:absolute;left:0;top:1040px;width:1200px;height:336px;
    background:linear-gradient(180deg,#e7a25b 0%,#c27a62 30%,#3c4f7a 62%,#1e2b4a 100%)}
  .mission__label{position:absolute;left:14px;top:40px;color:var(--orange);font-weight:700;font-size:22px;
    background:rgba(0,0,0,.25);padding:4px 10px}
  .mission__text{position:absolute;left:14px;top:88px;width:520px;color:var(--white);font-style:italic;
    font-weight:600;font-size:18px;line-height:1.35;background:rgba(0,0,0,.3);padding:4px 10px}

  .site-foot{position:absolute;left:0;top:2064px;width:1200px;height:112px;background:var(--footer);
    display:flex;align-items:center;padding:0 64px;color:var(--white)}
  .site-foot__social{display:flex;gap:40px}
  .site-foot__social span{width:30px;height:30px;border-radius:50%;background:var(--white)}
  .site-foot__web{position:absolute;left:680px;font-size:22px;font-weight:500;display:flex;align-items:center;gap:14px}
  .site-foot__web i{width:26px;height:26px;border-radius:50%;background:var(--white)}
</style>
</head>
<body>
  <div class="stage"></div>

  <section class="banner banner--header">
    <div class="banner__visual" role="img" aria-label="Photo of a woman on a city rooftop pushing away a large breaking steel chain against a bright blue sky"></div>
    <div class="banner__copy">
      <div class="banner__theme">Unrestrained</div>
      <div class="banner__year">2023</div>
      <div class="banner__rule"></div>
      <div class="banner__title">Lift Her Summit</div>
      <div class="banner__date">January 27, 2023</div>
      <div class="banner__venue"><svg viewBox="0 0 10 12"><path d="M5 0a4 4 0 0 0-4 4c0 3 4 8 4 8s4-5 4-8a4 4 0 0 0-4-4zm0 5.5a1.5 1.5 0 1 1 0-3 1.5 1.5 0 0 1 0 3z" fill="#fff"/></svg>Harborlight Stays Meeting Hall | San Marcos, TX</div>
    </div>
    <div class="banner__logo"><span class="banner__logo-dot"></span><span class="banner__logo-name">Q-BraTM</span></div>
  </section>

  <header class="site-head">
    <div class="site-logo"><span class="site-logo__dot"></span><span class="site-logo__name">Q-BraTM</span></div>
    <div class="site-login">Log in</div>
    <div class="site-search">
      <svg width="16" height="16" viewBox="0 0 16 16"><circle cx="6.5" cy="6.5" r="5" fill="none" stroke="#888" stroke-width="2"/><path d="M10 10l5 5" stroke="#888" stroke-width="2"/></svg>Search
    </div>
  </header>

  <nav class="site-nav">
    <span class="site-nav__home">HOME</span>
    <span>BLUEBONNET RESILIENCE FORUM<span class="site-nav__caret">▼</span></span>
    <span>ABOUT US<span class="site-nav__caret">▼</span></span>
    <span>MEMBERSHIP<span class="site-nav__caret">▼</span></span>
    <span>EVENTS<span class="site-nav__caret">▼</span></span>
    <span>CHAPTERS<span class="site-nav__caret">▼</span></span>
    <span class="site-nav__menu"><span></span><span></span><span></span></span>
  </nav>

  <section class="mission" role="img" aria-label="Photo of a city skyline and river at dusk">
    <div class="mission__label">OUR MISSION</div>
    <div class="mission__text">Evolve the capital projects industry through sharing of knowledge for optimized leadership, delivery and performance.</div>
  </section>

  <section class="banner banner--page">
    <div class="banner__visual" role="img" aria-label="Photo of a woman on a city rooftop pushing away a large breaking steel chain against a bright blue sky"></div>
    <div class="banner__copy">
      <div class="banner__theme">Unrestrained</div>
      <div class="banner__year">2023</div>
      <div class="banner__rule"></div>
      <div class="banner__title">Lift Her Summit</div>
      <div class="banner__date">January 27, 2023</div>
      <div class="banner__venue"><svg viewBox="0 0 10 12"><path d="M5 0a4 4 0 0 0-4 4c0 3 4 8 4 8s4-5 4-8a4 4 0 0 0-4-4zm0 5.5a1.5 1.5 0 1 1 0-3 1.5 1.5 0 0 1 0 3z" fill="#fff"/></svg>Harborlight Stays Meeting Hall | San Marcos, TX</div>
    </div>
    <div class="banner__logo"><span class="banner__logo-dot"></span><span class="banner__logo-name">Q-BraTM</span></div>
  </section>

  <footer class="site-foot">
    <div class="site-foot__social"><span></span><span></span><span></span></div>
    <div class="site-foot__web"><i></i>Q-BraTM.org</div>
  </footer>
</body>
</html>
```